Single Webpage Custom Design

We need a single webpage design (no coding) that uses our color and design scheme (http://awareness.morvantshield.com/).
We attached a draft that outlines the structure and content of what the page should look like.
As shown in the draft we need the following sections (in that order):
- Graphic with Text & Logo on top
- Product Explanation
- Customer Logos
- Success Stories with logo and citation each
- Contact form
- Footer

```html
<!DOCTYPE html>
<html lang="de">
<head>
<meta charset="utf-8">
<title>Morvant – Human Firewall</title>
<link rel="stylesheet" href="https://fonts.googleapis.com/css2?family=Montserrat:wght@400;500;600;700;800&family=Roboto:wght@400;500;700&display=swap">
<style>
:root{
  --teal:#22b3bb;
  --teal-light:#3cc4c9;
  --teal-dark:#0e7f89;
  --orange:#f6a123;
  --navy:#17323f;
  --ink:#333b40;
  --muted:#7a8287;
  --line:#dfe4e6;
  --white:#ffffff;
  --grey:#a9a9a9;
  --footer-bg:#ffffff;
  --copy-bg:#eeeeee;
}
*{box-sizing:border-box;margin:0;padding:0}
html,body{width:1200px;height:4032px;overflow:hidden}
body{position:relative;font-family:"Montserrat",sans-serif;color:var(--ink);background:var(--white)}
.abs{position:absolute}
h2.section-title{position:absolute;left:0;width:1200px;text-align:center;font-family:"Roboto",sans-serif;font-weight:700;font-size:27px;letter-spacing:.2px}
.title-rule{position:absolute;left:585px;width:30px;height:3px;background:var(--orange)}

/* hero */
.hero{position:absolute;left:0;top:0;width:1200px;height:782px;background:linear-gradient(115deg,#2bb9c0 0%,#1aa7b1 55%,#139aa6 100%)}
.hero-photo{position:absolute;left:820px;top:70px;width:380px;height:626px;background:linear-gradient(180deg,#5f8c8a 0%,#8d5f45 45%,#2c8f8f 100%);border-radius:180px 0 0 0;opacity:.85}
.brand{position:absolute;left:130px;top:34px;display:flex;align-items:center;gap:10px}
.brand-dot{width:34px;height:34px;border-radius:50%;background:var(--orange)}
.brand-name{font-family:"Montserrat",sans-serif;font-weight:800;font-size:28px;color:var(--navy)}
.main-nav{position:absolute;top:33px;left:0;width:1200px;font-family:"Roboto",sans-serif;font-size:13px;color:var(--white);font-weight:500}
.main-nav span{position:absolute}
.main-nav .active::after{content:"";position:absolute;left:0;right:0;top:-33px;height:3px;background:var(--white)}
.hero h1{position:absolute;left:128px;top:172px;font-family:"Roboto",sans-serif;font-weight:700;font-size:44px;color:var(--white);letter-spacing:.3px}
.hero-lead{position:absolute;left:128px;top:234px;width:540px;font-family:"Roboto",sans-serif;font-size:24px;line-height:32px;color:var(--white);font-weight:400}
.benefits{position:absolute;left:402px;top:362px;list-style:none;font-family:"Montserrat",sans-serif;font-weight:600;font-size:14.5px;color:var(--white)}
.benefits li{display:flex;align-items:center;gap:9px;height:35.5px}
.tick{width:17px;height:17px;border-radius:50%;background:var(--white);display:inline-flex;align-items:center;justify-content:center}
.chart{position:absolute;left:120px;top:375px}
.award-band{position:absolute;left:0;top:696px;width:1200px;height:86px;background:rgba(40,190,196,.85)}
.award{position:absolute;top:20px;display:flex;align-items:center;gap:14px;color:var(--white);font-size:10.5px;font-weight:600;line-height:15px}
.award-mark{width:40px;height:40px;border:2px solid var(--white);border-radius:50%;flex:none}

/* steps */
.connector{position:absolute;left:0;top:890px}
.step-card{position:absolute;top:970px;width:325px;height:250px;background:var(--white);border:1px solid var(--line);box-shadow:0 3px 10px rgba(0,0,0,.05)}
.step-badge{position:absolute;left:-12px;top:18px;width:68px;height:62px;border-radius:6px;color:var(--white);font-family:"Roboto",sans-serif;text-align:center;padding-top:10px;font-size:13px;line-height:18px}
.step-badge b{display:block;font-size:20px;font-weight:700}
.step-card h3{position:absolute;left:72px;top:30px;font-size:13.5px;font-weight:700;color:var(--teal)}
.step-sub{position:absolute;left:72px;top:56px;width:240px;padding-left:9px;border-left:2px solid var(--teal);font-size:8.8px;line-height:13px;font-weight:700;color:var(--ink)}
.step-text{position:absolute;left:72px;top:112px;width:240px;font-size:10px;line-height:16px;color:var(--muted)}
.step-item{position:absolute;left:72px;width:240px;display:flex;gap:10px;font-size:8.8px;line-height:12px;color:var(--muted)}
.step-icon{width:17px;height:17px;border:1.5px solid var(--orange);border-radius:3px;flex:none}

/* custom */
.custom{position:absolute;left:0;top:1314px;width:1200px;height:524px;background:linear-gradient(100deg,#3cc5ca 0%,#21acb6 50%,#0f7f8a 100%)}
.custom h2.section-title{top:64px;color:var(--white)}
.custom-intro{position:absolute;left:160px;top:130px;width:880px;text-align:center;color:var(--white);font-size:13.4px;line-height:23px}
.example-card{position:absolute;top:227px;height:219px;background:var(--white);box-shadow:0 4px 12px rgba(0,0,0,.12)}
.example-card h3{position:absolute;font-family:"Roboto",sans-serif;font-weight:700;font-size:16px;color:var(--orange);line-height:22px}
.example-card p{position:absolute;font-size:11.3px;line-height:20px;color:var(--muted)}
.ceo-photo{position:absolute;left:248px;top:34px;width:180px;height:148px;border-radius:50% 45% 55% 48%;background:linear-gradient(135deg,#e9ecee,#9aa2a6)}
.policy-shot{position:absolute;left:22px;top:42px;width:190px;height:134px;background:linear-gradient(180deg,#f4f6f7,#dfe3e5);border:1px solid var(--line)}

/* customers */
.customer-logo{position:absolute;display:flex;align-items:center;gap:8px;font-family:"Montserrat",sans-serif;font-weight:700;font-size:21px;color:var(--navy)}
.logo-sq{width:20px;height:20px;background:var(--navy)}

/* success */
.success{position:absolute;left:0;top:2378px;width:1200px;height:485px;background:linear-gradient(180deg,#1fb0b8,#2cbcc3)}
.success h2.section-title{top:60px;color:var(--white)}
.story{position:absolute;top:142px;width:441px;height:251px;border:2px solid rgba(255,255,255,.7);border-radius:3px;text-align:center;color:var(--white)}
.story-brand{margin-top:30px;display:inline-flex;align-items:center;gap:10px;font-weight:700;font-size:28px}
.story-brand i{width:34px;height:34px;border-radius:50%;background:var(--white);display:inline-block}
.story q{display:block;margin:20px auto 0;width:350px;font-size:15px;line-height:23px;quotes:none}
.story q::before,.story q::after{content:"\201C";font-size:30px;font-family:"Roboto",sans-serif;font-weight:700;vertical-align:-8px;margin-right:4px}
.story q::after{content:"\201D";margin-left:4px}
.btn-read{display:inline-block;margin-top:18px;width:128px;height:34px;line-height:34px;border-radius:17px;background:var(--orange);font-size:12px;font-weight:600;color:var(--white)}
.arrow{position:absolute;top:2625px}

/* contact */
.contact{position:absolute;left:0;top:2863px;width:1200px;height:634px;background:linear-gradient(120deg,#2f4a55 0%,#1f3c48 50%,#17313c 100%)}
.contact h2.section-title{top:96px;color:var(--white)}
.field{position:absolute;background:var(--white);border:1px solid #cfd6d9;font-size:14px;color:#9aa3a7;padding:19px 22px}
.submit{position:absolute;left:513px;top:510px;width:191px;height:51px;border-radius:26px;background:var(--orange);color:var(--white);font-weight:700;font-size:18px;display:flex;align-items:center;justify-content:center;gap:8px}

/* footer */
.footer{position:absolute;left:0;top:3497px;width:1200px;height:469px;background:var(--footer-bg)}
.footer h4{position:absolute;font-family:"Roboto",sans-serif;font-weight:700;font-size:14px;color:var(--navy);padding-bottom:5px;border-bottom:2px solid var(--teal)}
.footer .col-text{position:absolute;font-size:11.8px;line-height:20.5px;color:#4c555a}
.footer .col-text b{font-weight:700;color:var(--navy)}
.search-box{position:absolute;left:446px;top:113px;width:215px;height:33px;border:1px solid #b8c1c5;font-size:10.5px;color:#8a9396;padding:9px 12px}
.social{position:absolute;left:446px;display:flex;align-items:center;gap:14px;font-size:12.5px;color:#4c555a}
.social i{width:32px;height:32px;border-radius:50%;background:var(--teal);display:inline-block}
.info-links{position:absolute;left:744px;top:115px;list-style:none;font-size:11.8px;line-height:30.3px;color:#4c555a}
.lang-select{position:absolute;left:937px;top:118px;width:143px;height:31px;border:1px solid #b8c1c5;font-size:11px;padding:8px 14px;color:#4c555a}
.copy{position:absolute;left:0;top:3966px;width:1200px;height:66px;background:var(--copy-bg);text-align:center;line-height:66px;font-size:12px;color:#6a7378}
</style>
</head>
<body>

<!-- Hero -->
<header class="hero">
  <div class="hero-photo" role="img" aria-label="Photo of a confident woman in a brick-wall top and teal cape, arms on hips"></div>
  <div class="brand"><span class="brand-dot"></span><span class="brand-name">Morvant</span></div>
  <nav class="main-nav">
    <span class="active" style="left:546px">HOME</span>
    <span style="left:652px">SOLUTION</span>
    <span style="left:784px">PRICING</span>
    <span style="left:903px">ABOUT</span>
    <span style="left:1014px">CONTACT</span>
  </nav>
  <h1>HUMAN FIREWALL</h1>
  <p class="hero-lead">Mittels Cyber Awareness Schulungen das Risiko von Attacken innerhalb von 12 Monaten messbar um 50% senken</p>
  <ul class="benefits">
    <li><span class="tick"><svg width="10" height="10" viewBox="0 0 10 10"><path d="M1.5 5.2l2.3 2.3 4.7-5" fill="none" stroke="#22b3bb" stroke-width="1.8"/></svg></span>Mit Geld Zuruck Garantie!</li>
    <li><span class="tick"><svg width="10" height="10" viewBox="0 0 10 10"><path d="M1.5 5.2l2.3 2.3 4.7-5" fill="none" stroke="#22b3bb" stroke-width="1.8"/></svg></span>Individualisierbare Inhalte</li>
    <li><span class="tick"><svg width="10" height="10" viewBox="0 0 10 10"><path d="M1.5 5.2l2.3 2.3 4.7-5" fill="none" stroke="#22b3bb" stroke-width="1.8"/></svg></span>Preiswerte Losung</li>
    <li><span class="tick"><svg width="10" height="10" viewBox="0 0 10 10"><path d="M1.5 5.2l2.3 2.3 4.7-5" fill="none" stroke="#22b3bb" stroke-width="1.8"/></svg></span>Datenschutzkonformk</li>
  </ul>
  <svg class="chart" width="430" height="275" viewBox="0 0 430 275">
    <g fill="none" stroke="#ffffff" stroke-width="1.2" opacity=".8">
      <path d="M25 30 V238 H370"/>
    </g>
    <text x="12" x2="0" y="50" transform="rotate(-90 12 50)" fill="#fff" font-size="10" font-family="Roboto,sans-serif">RISK</text>
    <text x="378" y="246" fill="#fff" font-size="10" font-family="Roboto,sans-serif">TIME</text>
    <g fill="#bfeef0" opacity=".85">
      <rect x="46" y="35" width="56" height="203"/>
      <rect x="126" y="112" width="56" height="126"/>
      <rect x="203" y="151" width="53" height="87"/>
      <rect x="279" y="190" width="56" height="48"/>
    </g>
    <g fill="#f6a123">
      <path d="M46 35 L74 20 L102 35 L74 48Z"/>
      <path d="M126 112 L154 97 L182 112 L154 125Z"/>
      <path d="M203 151 L229 136 L256 151 L229 164Z"/>
      <path d="M279 190 L307 175 L335 190 L307 203Z"/>
    </g>
    <path d="M74 34 C110 80 130 110 170 122 S250 150 300 185" fill="none" stroke="#ffffff" stroke-width="2"/>
    <g fill="#fff" font-size="8.5" font-weight="700" font-family="Montserrat,sans-serif" text-anchor="middle">
      <text x="62" y="256">GENERIC</text><text x="62" y="266">TRAINING</text>
      <text x="150" y="253">ATTACK</text><text x="150" y="263">SIMULATION</text>
      <text x="225" y="256">SECURITY</text><text x="225" y="266">GAME</text>
      <text x="297" y="253">ROLE BASED</text><text x="297" y="263">TRAINING</text>
    </g>
  </svg>
  <div class="award-band">
    <div class="award" style="left:112px"><span class="award-mark"></span><span>In 2020, MORVANT won the Digital Defense<br>Excellence Award for Best Anti Phishing</span></div>
    <div class="award" style="left:422px"><span class="award-mark"></span><span>In 2020, MORVANT won the Digital Defense Excellence<br>Award for the Best "Security Education Platform"</span></div>
    <div class="award" style="left:798px"><span class="award-mark"></span><span>2020 Gold Winner "Cyber Security Education<br>and Training" in the Secure Tech Review guide</span></div>
  </div>
</header>

<!-- How it works -->
<h2 class="section-title" style="top:843px;color:var(--navy)">HOW DOES IT WORK?</h2>
<svg class="connector" width="1200" height="70" viewBox="0 0 1200 70">
  <g fill="none" stroke="#22b3bb" stroke-width="1.3" stroke-dasharray="3 3">
    <path d="M600 0 V26 M275 26 H957 M275 26 V60 M600 26 V60 M957 26 V60"/>
  </g>
  <g fill="#fff" stroke="#22b3bb" stroke-width="2">
    <circle cx="275" cy="64" r="4"/><circle cx="600" cy="64" r="4"/><circle cx="957" cy="64" r="4"/>
  </g>
</svg>

<article class="step-card" style="left:105px">
  <div class="step-badge" style="background:var(--grey)">STEP<b>№1</b></div>
  <h3>SET GOALS &amp; CREATE A PLAN</h3>
  <p class="step-sub">UNDERSTNDING YOUR GOALS WILL DEFINE PROGRAM SCOPE</p>
  <p class="step-text" style="top:100px">Lorem Ipsum is simply dummy text of the printing and typesetting industry. Lorem Ipsum</p>
  <div class="step-item" style="top:146px"><span class="step-icon" style="border-color:var(--grey)"></span>Lorem Ipsum is simply dummy text of the printing and typesetting industry.</div>
  <div class="step-item" style="top:180px"><span class="step-icon" style="border-color:var(--grey)"></span>Lorem Ipsum is simply dummy text of the printing and typesetting industry.</div>
</article>
<article class="step-card" style="left:451px">
  <div class="step-badge" style="background:var(--orange)">STEP<b>№2</b></div>
  <h3>ASSESS AWEARENESS LEVEL</h3>
  <p class="step-sub">USE PHISHING SIMULATIONS OR ASSESSMENTS TO UNDERTAND THE CURRENT AWARENESS LEVEL</p>
  <p class="step-text" style="top:112px">Lorem Ipsum is simply dummy text of the printing and typesetting industry. Lorem Ipsum</p>
  <div class="step-item" style="top:158px"><span class="step-icon"></span>Lorem Ipsum is simply dummy text of the printing and typesetting industry.</div>
  <div class="step-item" style="top:192px"><span class="step-icon"></span>Lorem Ipsum is simply dummy text of the printing and typesetting industry.</div>
</article>
<article class="step-card" style="left:795px">
  <div class="step-badge" style="background:var(--teal)">STEP<b>№3</b></div>
  <h3>RUN THE AWARENESS CAMPAIGN</h3>
  <p class="step-sub">IMPROVE THE SECURITY AWARENESS LEVEL WITH TAILORED CORSES. OPTIMIZE THE PROGRAM OVER TIME</p>
  <p class="step-text" style="top:112px">Lorem Ipsum is simply dummy text of the printing and typesetting industry.</p>
  <div class="step-item" style="top:158px"><span class="step-icon" style="border-color:var(--teal)"></span>Lorem Ipsum is simply dummy text of the printing and typesetting industry.</div>
  <div class="step-item" style="top:192px"><span class="step-icon" style="border-color:var(--teal)"></span>Lorem Ipsum is simply dummy text of the printing and typesetting industry.</div>
</article>

<svg class="abs" style="left:0;top:1252px" width="1200" height="62" viewBox="0 0 1200 62"><path d="M700 62 L1200 0 V62Z" fill="#f6a123"/></svg>

<!-- Customizable -->
<section class="custom">
  <h2 class="section-title">FULLY CUSTOMIZABLE!</h2>
  <p class="custom-intro">You Might Ask: WHy do the Trainings need customization? In &nbsp;Addition to adjusting the design (Logo, Font, Colors) to Your Corporate Look and feel, It is Important that your emploees perceive the training as soemthing they can relate to.<br>EXAMPLES:</p>
  <div class="example-card" style="left:133px;width:457px">
    <h3 style="left:37px;top:46px">FROM CEO:</h3>
    <p style="left:37px;top:80px;width:200px">Add a personal greeting message from your CEO at the start of the course to highlight the importance of the training.</p>
    <div class="ceo-photo" role="img" aria-label="Photo of a laptop on a desk showing a video greeting"></div>
  </div>
  <div class="example-card" style="left:607px;width:458px">
    <div class="policy-shot" role="img" aria-label="Screenshot of an internal policy document page"></div>
    <h3 style="left:238px;top:46px;width:200px">DO YOU KNOW OUR POLICIES?</h3>
    <p style="left:238px;top:98px;width:205px">You could ask the user to read and acknowledge your internal policies prior to starting the course.</p>
  </div>
</section>
<svg class="abs" style="left:0;top:1838px" width="1200" height="70" viewBox="0 0 1200 70"><path d="M0 0 H475 L0 68Z" fill="#f6a123"/></svg>

<!-- Customers -->
<h2 class="section-title" style="top:1950px;color:var(--navy);font-size:25px">MEHR ALS <span style="color:var(--orange)">400</span> KUNDEN VERTRAUEN BEREITS AUF MORVANT:</h2>
<div class="title-rule" style="top:1991px"></div>
<div class="customer-logo" style="left:138px;top:2072px">Alvenor</div>
<div class="customer-logo" style="left:396px;top:2072px">Kestrel Informatik</div>
<div class="customer-logo" style="left:628px;top:2072px"><span class="logo-sq"></span>Stadtwerk Nordhal</div>
<div class="customer-logo" style="left:866px;top:2072px">Railmont</div>
<div class="customer-logo" style="left:1016px;top:2072px">Quorva</div>
<div class="customer-logo" style="left:222px;top:2200px">Tessling</div>
<div class="customer-logo" style="left:436px;top:2200px">Veridane</div>
<div class="customer-logo" style="left:630px;top:2200px">die Heimsicher</div>
<div class="customer-logo" style="left:852px;top:2200px"><span class="logo-sq"></span>Brantec</div>

<svg class="abs" style="left:0;top:2315px" width="1200" height="63" viewBox="0 0 1200 63"><path d="M0 0 L480 63 H0Z" fill="#f6a123"/></svg>

<!-- Success stories -->
<section class="success">
  <h2 class="section-title">SUCCESS STORIES</h2>
  <div class="story" style="left:146px">
    <div class="story-brand"><i></i>Aerolind</div>
    <q>Morvant bietet ein optimales Gesamtpaket, mit dem wir die Awareness bei unseren Mitarbeitern dauehaft hochhalten konnen</q>
    <span class="btn-read">Read More</span>
  </div>
  <div class="story" style="left:618px">
    <div class="story-brand"><i></i>Glacio Foods</div>
    <q>Es ist einfach ein tolles Gefuhl, wenn man sieht, dass die Mitarbeiter deutlich wachsamer geworden sind</q>
    <span class="btn-read">Read More</span>
  </div>
</section>
<svg class="arrow" style="left:78px" width="22" height="40" viewBox="0 0 22 40"><path d="M18 3 L4 20 L18 37" fill="none" stroke="#fff" stroke-width="3.5"/></svg>
<svg class="arrow" style="left:1098px" width="22" height="40" viewBox="0 0 22 40"><path d="M4 3 L18 20 L4 37" fill="none" stroke="#fff" stroke-width="3.5"/></svg>

<!-- Contact -->
<section class="contact">
  <div class="abs" role="img" aria-label="Dim photo of a team of business people at work" style="left:0;top:0;width:1200px;height:634px;background:linear-gradient(90deg,rgba(60,90,100,.35),rgba(20,45,55,.2),rgba(60,90,100,.35))"></div>
  <svg class="abs" style="left:0;top:0" width="1200" height="70" viewBox="0 0 1200 70"><path d="M690 0 H1200 V68Z" fill="#f6a123"/></svg>
  <h2 class="section-title">GET IN TOUCH WITH US</h2>
  <div class="title-rule" style="top:142px"></div>
  <div class="field" style="left:133px;top:172px;width:462px;height:55px">Full Name*</div>
  <div class="field" style="left:609px;top:172px;width:464px;height:55px">Your Email*</div>
  <div class="field" style="left:133px;top:242px;width:462px;height:55px">Phone</div>
  <div class="field" style="left:609px;top:242px;width:464px;height:55px">Subject*</div>
  <div class="field" style="left:133px;top:310px;width:462px;height:55px">Country</div>
  <div class="field" style="left:609px;top:310px;width:464px;height:55px">Location</div>
  <div class="field" style="left:133px;top:378px;width:940px;height:113px">Message*</div>
  <div class="submit">Submit <svg width="9" height="13" viewBox="0 0 9 13"><path d="M2 1.5 L7 6.5 L2 11.5" fill="none" stroke="#fff" stroke-width="2"/></svg></div>
</section>

<!-- Footer -->
<footer class="footer">
  <h4 style="left:124px;top:76px">CONTACTS</h4>
  <div class="col-text" style="left:124px;top:110px;width:290px">
    <b>Address: Europe</b><br>Morvant Shield AG Talweg 18<br>6340 Baar Switzerland<br><br>
    <b>Address: North America</b><br>MORVANT Shield USA 4410 Cedar Park Ave<br>Suite 210 Denton, TX 76201<br><br>
    Phone Global: +41 44 555 01 28<br>Phone USA: +1-555-014-2207<br>Phone USA Support: +1-555-014-2219<br>Phone Canand: +1 555-018-3344<br>Phone France: +33 655 500 412<br>Phone UK: +44(0) 7700 900512
  </div>
  <h4 style="left:446px;top:78px">SEARCH</h4>
  <div class="search-box">Search
    <svg class="abs" style="right:9px;top:8px" width="15" height="15" viewBox="0 0 15 15"><circle cx="6" cy="6" r="4.5" fill="none" stroke="#22b3bb" stroke-width="2"/><path d="M9.5 9.5 L13.5 13.5" stroke="#22b3bb" stroke-width="2"/></svg>
  </div>
  <h4 style="left:446px;top:178px">CONNECT</h4>
  <div class="social" style="top:220px"><i></i>Circlenet</div>
  <div class="social" style="top:268px"><i></i>Chirper</div>
  <div class="social" style="top:316px"><i></i>Vidstream</div>
  <div class="social" style="top:364px"><i></i>Linkwork</div>
  <h4 style="left:744px;top:80px">INFOMATION</h4>
  <ul class="info-links">
    <li>Home</li><li>Solution</li><li>Pricing</li><li>Resources</li><li>About Us</li><li>Support Wiki</li><li>Contact</li><li>Download MORVANT</li><li>Demo Request</li>
  </ul>
  <h4 style="left:937px;top:77px">LANGUAGE</h4>
  <div class="lang-select">English
    <svg class="abs" style="right:12px;top:12px" width="9" height="6" viewBox="0 0 9 6"><path d="M0 0 H9 L4.5 6Z" fill="#333b40"/></svg>
  </div>
  <div class="brand" style="left:937px;top:235px"><span class="brand-dot"></span><span class="brand-name">Morvant</span></div>
</footer>
<div class="copy">© Morvant All Rights Reserved 2021</div>

</body>
</html>
```